Website Design Project for Beauty & Wellness Professionals

As background information, I have a website that is focused on Beauty & Wellness Professionals:
- Job Search (www.trilhavelora.com)
- Business Classifieds (negocios.trilhavelora.com)
- Freelancer Classifieds (freelancer.trilhavelora.com)
- Course Reviews (cursos.trilhavelora.com)

All those websites use standard templates.

I need a DESIGN for the HOME PAGE (no coding) of the Website Platform that consolidates the four platforms under the same design.

Website designs that we like:
- nestorly.com
- workpane.com

Target Market(s)

Brazilian Professionals from Beauty & Wellness sector

Industry/Entity Type

Business

Requirements
Must have
• Website designs that we like:
- nestorly.com
- workpane.com

```html
<!DOCTYPE html>
<html lang="en">
<head>
<meta charset="utf-8">
<title>Trilha Velora – Beauty &amp; Wellness Professionals</title>
<link rel="stylesheet" href="https://fonts.googleapis.com/css2?family=Archivo+Black&family=Arimo:wght@400;700&display=swap">
<style>
:root{
  --green:#6db26e;
  --ink:#222222;
  --text:#555555;
  --rust:#9c4a26;
  --brown-link:#9a5a3a;
  --panel:#f2f2f2;
  --rule:#e4e4e4;
  --footer:#2b2b2b;
  --footer-text:#c4c4c4;
  --white:#ffffff;
  --logo:#4aa9bf;
}
*{margin:0;padding:0;box-sizing:border-box}
html,body{width:765px;height:1200px;overflow:hidden;background:var(--white)}
body{position:relative;font-family:"Arimo",Arial,sans-serif;color:var(--text)}
.abs{position:absolute}

.topline{left:0;top:0;width:765px;height:3px;background:var(--green)}
.brand{left:90px;top:14px;display:flex;align-items:center;gap:8px}
.brand-dot{width:30px;height:30px;border-radius:50%;background:var(--logo)}
.brand-name{font-size:20px;color:var(--logo);font-weight:400}
.nav{left:325px;top:3px;height:55px;display:flex;list-style:none}
.nav li{font-size:9.7px;color:#333;text-transform:uppercase;line-height:55px;padding:0 13.5px}
.nav li.active{background:var(--green);color:var(--white);padding:0 14px}

.hero{left:0;top:58px;width:765px;height:270px;background:linear-gradient(90deg,#9fc7cc 0%,#c8dcdc 35%,#bdd2c5 60%,#5f8f78 85%,#3d4a45 100%)}
.book-title{left:468px;top:80px;font-family:"Archivo Black",sans-serif;font-size:16px;color:var(--white);transform:scaleX(.84);transform-origin:left top;white-space:nowrap}
.book-form{left:470px;top:111px;width:206px;height:204px;border:2px solid var(--white);border-radius:6px;background:rgba(160,118,80,.88)}
.book-form label{position:absolute;left:6px;font-size:10px;color:var(--white)}
.book-form .field{position:absolute;left:41px;width:147px;height:22px;background:var(--white);border-radius:3px}
.submit{left:77px;top:162px;width:66px;height:26px;background:var(--green);border:2px solid var(--white);border-radius:3px;color:var(--white);font-weight:700;font-size:12px;text-align:center;line-height:22px;letter-spacing:.5px}

.pros{left:0;top:328px;width:765px;height:203px;background:var(--panel)}
.pros-title{left:88px;top:346px;font-size:14px;color:#333;font-weight:400}
.card{top:381px;width:137px;height:111px;border:2px solid #cfcfcf;border-radius:7px;background:var(--white)}
.card .photo{position:absolute;left:2px;top:3px;width:129px;height:103px;border-radius:3px}
.card .band{position:absolute;left:2px;top:3px;width:129px;height:36px;background:rgba(70,70,70,.8);border-radius:3px 3px 0 0;color:var(--white);font-weight:700;font-size:12px;line-height:14px;text-align:center;padding-top:4px;letter-spacing:.6px}
.click{top:499px;width:137px;text-align:center;font-size:9.5px;font-weight:700;color:var(--brown-link);text-decoration:underline;letter-spacing:.5px}

.welcome-frame{left:88px;top:562px;width:188px;height:128px;border:1px solid #ddd;padding:6px}
.welcome-frame div{width:100%;height:100%;background:linear-gradient(135deg,#e8c4ad,#d9a48a 55%,#f1ddd0)}
.welcome-h{left:292px;top:560px;font-family:"Archivo Black",sans-serif;font-size:28px;color:var(--ink);line-height:32px;font-weight:400}
.welcome-sub{left:292px;top:594px;width:380px;font-family:"Archivo Black",sans-serif;font-size:14px;line-height:17px;color:#333;font-weight:400}
.welcome-p{left:292px;top:629px;width:372px;font-size:8.6px;line-height:12.8px;color:var(--text);hyphens:auto;-webkit-hyphens:auto}
.rule{left:88px;top:723px;width:588px;height:1px;background:var(--rule)}

.col{top:752px;width:175px}
.col h2{font-family:"Archivo Black",sans-serif;font-size:15px;color:var(--ink);font-weight:400;height:31px}
.col .img{width:175px;height:106px}
.col p{font-size:8.2px;line-height:12.7px;margin-top:14px;text-align:justify;hyphens:auto;-webkit-hyphens:auto}
.col p.body{font-size:8px;line-height:12.6px}
.col ul{list-style:none;margin-top:9px}
.col li{font-size:8.3px;line-height:21.3px;display:flex;align-items:center;gap:7px}
.col li svg{flex:none}
.col .sub{color:#222;margin-top:14px;font-size:8.2px}
.col .sub + p{margin-top:1px}
.btn{top:1053px;width:46px;height:25px;background:var(--rust);border-radius:3px;color:var(--white);font-size:10px;text-align:center;line-height:25px}

.footer{left:0;top:1116px;width:765px;height:84px;background:var(--footer)}
.foot-nav{left:88px;top:1135px;display:flex;font-size:9px;color:var(--footer-text)}
.foot-nav .sep{margin:0 13px}
.social{left:576px;top:1130px;display:flex;gap:5px}
.social span{width:19px;height:19px;border-radius:50%;background:#8a8a8a}
.copy{left:88px;top:1167px;font-size:7px;color:#888}
</style>
</head>
<body>
<div class="abs topline"></div>
<header>
  <div class="abs brand"><span class="brand-dot"></span><span class="brand-name">Trilha Velora</span></div>
  <ul class="abs nav">
    <li class="active">Home</li><li>About Us</li><li>Services</li><li>Gallery</li><li>Contact Us</li>
  </ul>
</header>

<section class="abs hero" role="img" aria-label="Spa photo of a woman resting on a white towel holding a pink lotus flower, soft teal and green leaf background"></section>
<div class="abs book-title">BOOK YOUR APPOINTMENT</div>
<form class="abs book-form">
  <label style="top:24px">Stylist:</label><span class="field" style="top:19px"></span>
  <label style="top:51px">Date:</label><span class="field" style="top:46px"></span>
  <label style="top:78px">Time:</label><span class="field" style="top:73px"></span>
  <label style="top:104px">Salon:</label><span class="field" style="top:100px;height:52px"></span>
  <div class="abs submit">SUBMIT</div>
</form>

<section class="abs pros"></section>
<h1 class="abs pros-title">BEAUTY &amp; WELLNESS PROFESSIONALS</h1>
<div class="abs card" style="left:87px"><div class="photo" role="img" aria-label="Woman with flowers" style="background:linear-gradient(135deg,#f3e3dc,#e2b9a6)"></div><div class="band">JOB<br>SEARCH</div></div>
<div class="abs card" style="left:239px"><div class="photo" role="img" aria-label="Woman relaxing at a spa with lotus" style="background:linear-gradient(135deg,#b07a55,#d9b08c)"></div><div class="band">BUSINESS<br>CLASSIFIEDS</div></div>
<div class="abs card" style="left:390px"><div class="photo" role="img" aria-label="Makeup brushes and powder" style="background:linear-gradient(135deg,#e9d8c6,#c99d7a)"></div><div class="band">FREELANCER<br>CLASSIFIEDS</div></div>
<div class="abs card" style="left:541px"><div class="photo" role="img" aria-label="Close-up of eyes" style="background:linear-gradient(135deg,#d4a98c,#9c6b50)"></div><div class="band">COURSE<br>REVIEWS</div></div>
<div class="abs click" style="left:88px">CLICK HERE</div>
<div class="abs click" style="left:240px">CLICK HERE</div>
<div class="abs click" style="left:391px">CLICK HERE</div>
<div class="abs click" style="left:542px">CLICK HERE</div>

<div class="abs welcome-frame"><div role="img" aria-label="Portrait of a woman with pink eye makeup"></div></div>
<h2 class="abs welcome-h">WELCOME !</h2>
<h3 class="abs welcome-sub">IN PEDE MI, ALIQUET SIT AMET, EUISMOD IN,AUCTOR UT, LIGULA</h3>
<p class="abs welcome-p">Nulla ut tempus quam. Aenean augue eros, placerat quis interdum eu, varius vel urna. Fusce vitae posuere nulla, a pellentesque mi. Suspendisse potenti. Praesent mi sapien, dictum a scelerisque nec, vulputate ut felis. In consectetur auctor justo, commodo sollicitudin erat tristique et. Mauris dui augue, facilisis a tristique ut, lacinia in dui. Nam velit justo, malesuada vitae lacus at, dictum tempus sem.</p>
<div class="abs rule"></div>

<div class="abs col" style="left:88px">
  <h2>WHY CHOOSE US</h2>
  <div class="img" role="img" aria-label="Woman in a white towel receiving a massage" style="background:linear-gradient(135deg,#efe4da,#d8b9a0)"></div>
  <p class="body">Ut tristique tellus eu faucibus aliquet. Duis venenatis ultrices lorem ac elementum. Ut laoreet leo sed dapibus mattis. Nulla ac egestas ante. Cras sit amet purus adipiscing, egestas ligula nec, suscipit arcu. Suspendisse sed rutrum risus. Sed accumsan arcu sagittis quam varius dignissim. Suspendisse ante diam, tincidunt at faucibus ut, placerat a eros. Praesent adipiscing semper diam, ut dictum eros feugiat id. Class aptent taciti sociosqu ad litora torquent per conubia nostra, per inceptos himenaeos.</p>
</div>
<div class="abs col" style="left:296px">
  <h2>SERVICES</h2>
  <div class="img" role="img" aria-label="Woman posing with bare shoulders on a peach background" style="background:linear-gradient(135deg,#fde5d3,#e9b99a)"></div>
  <ul>
    <li><svg width="4" height="6"><path d="M0 0L4 3L0 6Z" fill="#6db26e"/></svg>Sui blanditiistes es praetiuptatum</li>
    <li><svg width="4" height="6"><path d="M0 0L4 3L0 6Z" fill="#6db26e"/></svg>Welenitimos aliquqdoloires etres</li>
    <li><svg width="4" height="6"><path d="M0 0L4 3L0 6Z" fill="#6db26e"/></svg>Euamolestiasexceuri sint timilique</li>
    <li><svg width="4" height="6"><path d="M0 0L4 3L0 6Z" fill="#6db26e"/></svg>Suincupaqui officia deserunt</li>
    <li><svg width="4" height="6"><path d="M0 0L4 3L0 6Z" fill="#6db26e"/></svg>Aollianimid estlaborum et dolorum</li>
    <li><svg width="4" height="6"><path d="M0 0L4 3L0 6Z" fill="#6db26e"/></svg>Nassafugharum quidemed rerum</li>
    <li><svg width="4" height="6"><path d="M0 0L4 3L0 6Z" fill="#6db26e"/></svg>Suincupaqui officia deserunt</li>
  </ul>
</div>
<div class="abs col" style="left:501px">
  <h2>OUR MISSION</h2>
  <div class="img" role="img" aria-label="Collage of spa treatments, flowers and green face masks" style="background:linear-gradient(90deg,#c7a48c,#e8dccf 35%,#a7b55a 70%,#7a4a2e)"></div>
  <p class="sub">Sui blanditiistes es praetiuptatum</p>
  <p>Eenitimos alquqdolores etres quamolestiasex ceuri sint piditaprdentimilique suincupaqui officia deserunt.</p>
  <p class="sub">Aollianimid estlaborum et dolorum</p>
  <p>Massafugharum quidemed rerum facilis est et Nam libero tempore, cum soluta nobis est eligend.</p>
</div>
<div class="abs btn" style="left:88px">More</div>
<div class="abs btn" style="left:296px">More</div>
<div class="abs btn" style="left:501px">More</div>

<footer class="abs footer"></footer>
<nav class="abs foot-nav">
  <span>Home</span><span class="sep">|</span><span>About us</span><span class="sep">|</span><span>Services</span><span class="sep">|</span><span>Gallery</span><span class="sep">|</span><span>Blog</span><span class="sep">|</span><span>Contact us</span>
</nav>
<div class="abs social"><span></span><span></span><span></span><span></span></div>
<p class="abs copy">Copyright 2013 www.trilhavelora.com All Rights Reserved.</p>
</body>
</html>
```